Our product is called "BrisaVeil Antimicrobial Photosensitizer Mask." It is worn over the face by individuals who have respiratory infections. It releases singlet oxygen upon contact with visible light. So, this product will be sold to the healthcare industry and in retail establishments to individuals with respiratory infections.
This website must have the look and feel of being professional and clean. So, a white background is where I think I want this website to end up. Though, I am open to designs that have different color backgrounds like a light to medium gray or black.. In other words I prefer a white background, but I do not want to constrain the artists who might have other unique ideas about how the website should appear.
The logo files are attached to this brief. #ff3e81 is the hex color code that is used in the mask. The green shade in the cloud and light rays surrounding the mask should be used as well.
Target Market(s)
Health and wellness
Industry/Entity Type
Healthcare
Coding
Coded - Design and coding required
Number of Pages Required
5+ page
Requirements
Must have
- Pages: Home, Our Company, Contact, FAQ page, Order, Terms and Conditions, Legal

```html
<!DOCTYPE html>
<html lang="en">
<head>
<meta charset="utf-8">
<title>BrisaVeil Antimicrobial Photosensitizer Mask</title>
<link href="https://fonts.googleapis.com/css2?family=Montserrat:ital,wght@0,400;0,500;0,600;0,700;1,400;1,500&display=swap" rel="stylesheet">
<style>
:root{
  --pink:#e0185e;
  --ink:#3a3a3a;
  --body:#555;
  --mint:#eef7f0;
  --paper:#f6f7f9;
  --grey-btn:#9a9a9a;
  --footer-bar:#555555;
  --icon-green:#8fd49e;
  --brand-dot:#d8322f;
}
*{margin:0;padding:0;box-sizing:border-box}
html,body{width:1200px;height:5245px;overflow:hidden}
body{font-family:'Montserrat',sans-serif;color:var(--ink);background:#fff;position:relative}
section,header,footer{position:absolute;left:0;width:1200px}
.abs{position:absolute}
.accent{color:var(--pink)}
.rule{position:absolute;width:52px;height:3px;background:var(--pink)}
.btn{position:absolute;display:inline-block;border-radius:20px;color:#fff;font-weight:700;font-size:11px;letter-spacing:.4px;text-align:center;text-transform:uppercase}
.btn-pink{background:var(--pink)}
.btn-grey{background:var(--grey-btn)}
.section-title{position:absolute;left:0;width:1200px;text-align:center;font-size:38px;font-weight:400;color:var(--ink)}
.copy{position:absolute;font-size:17.5px;line-height:30px;color:var(--body)}
.art{position:absolute}

/* header */
.site-header{top:0;height:110px;background:#fff}
.brand-mark{left:56px;top:22px;width:72px;height:72px;border-radius:50%;background:var(--brand-dot)}
.brand-name{left:142px;top:48px;font-size:16px;font-weight:700;color:var(--pink)}
.main-nav{right:75px;top:48px;display:flex;gap:34px;font-size:11px;color:#333}
.main-nav .active{position:relative}
.main-nav .active::after{content:"";position:absolute;left:14px;right:14px;bottom:-9px;height:3px;background:var(--pink)}

/* hero */
.hero{top:100px;height:576px;background:linear-gradient(180deg,#f7f7f7 0%,#e4e4e4 45%,#a9a9a9 80%,#8a8a8a 100%)}
.hero h1{position:absolute;top:148px;width:1200px;text-align:center;font-size:51px;font-weight:700;color:var(--ink)}
.hero p{position:absolute;top:233px;width:1200px;text-align:center;font-size:22px;line-height:33px;color:#333}

/* how it works */
.how{top:676px;height:711px;background:var(--paper)}
/* benefits */
.benefits{top:1387px;height:748px;background:var(--mint)}
.benefit h3{position:absolute;font-size:29px;font-weight:400;line-height:36px;color:var(--ink)}
.benefit p{position:absolute;font-size:17.5px;line-height:30px;color:var(--body);width:252px}
/* healthcare */
.healthcare{top:2135px;height:635px;background:var(--paper)}
/* individuals */
.everyday{top:2770px;height:642px;background:var(--mint)}
/* testimonials */
.testimonials{top:3412px;height:576px;background:var(--paper)}
.quote-mark{position:absolute;font-size:90px;font-family:Georgia,serif;color:#bbb;line-height:1}
.arrow{position:absolute;width:24px;height:24px;border-right:5px solid #aaa;border-bottom:5px solid #aaa}
/* cta */
.cta{top:3988px;height:595px;background:var(--mint)}
.cta-box{position:absolute;left:189px;top:194px;width:821px;height:232px;background:var(--pink);border-radius:22px}
.cta-box p{position:absolute;top:76px;width:821px;text-align:center;color:#fff;font-size:21px;font-weight:600;line-height:32px}
/* footer */
.site-footer{top:4583px;height:550px;background:var(--paper)}
.foot-link{position:absolute;font-size:15px;color:#333}
.social{position:absolute;width:27px;height:27px;border-radius:50%;background:#333}
.foot-brand{left:888px;top:475px;font-size:16px;font-weight:700;color:var(--pink)}
.foot-bar{top:5133px;height:112px;background:var(--footer-bar)}
.foot-bar p{position:absolute;left:138px;top:47px;color:#eee;font-size:11px}
</style>
</head>
<body>

<header class="site-header">
  <div class="abs brand-mark" aria-hidden="true"></div>
  <div class="abs brand-name">BrisaVeil Antimicrobial Photosensitizer Mask</div>
  <nav class="abs main-nav">
    <span class="active">How It Works</span><span>Benefits</span><span>For Healthcare</span><span>For Individuals</span><span>FAQ</span><span>Contact Us</span>
  </nav>
</header>

<section class="hero" role="img" aria-label="Misty grey mountain range landscape">
  <h1>Protect Your Health, <span class="accent">Protect Others</span></h1>
  <p>BrisaVeil: Advanced Respiratory Mask with<br>Photosensitizer Technology</p>
  <span class="btn btn-pink" style="left:430px;top:338px;width:147px;height:30px;line-height:30px">Learn More</span>
  <span class="btn btn-grey" style="left:620px;top:338px;width:147px;height:30px;line-height:30px">Shop Now</span>
</section>

<section class="how">
  <h2 class="section-title" style="top:106px">How <span class="accent">BrisaVeil</span> Works</h2>
  <div class="art" role="img" aria-label="Illustration of a head wearing the respiratory mask releasing red particles" style="left:81px;top:220px;width:440px;height:377px;background:radial-gradient(ellipse at 45% 50%,#cfd2d6 0%,#e6e8eb 50%,var(--paper) 75%)"></div>
  <div class="rule" style="left:617px;top:290px"></div>
  <p class="copy" style="left:617px;top:310px;width:490px">BrisaVeil is a revolutionary mask designed for individuals with respiratory infections. By utilizing Rose Bengal photosensitizer technology, BrisaVeil releases singlet oxygen upon exposure to visible light. This powerful oxygen molecule helps to neutralize pathogens, enhancing protection for both the wearer and those around them.</p>
</section>

<section class="benefits">
  <h2 class="section-title" style="top:106px">How <span class="accent">BrisaVeil</span> Works</h2>

  <div class="benefit">
    <svg class="abs" style="left:81px;top:233px" width="122" height="122" viewBox="0 0 122 122" fill="none" stroke="var(--icon-green)" stroke-width="2">
      <rect x="4" y="38" width="114" height="76" rx="8"/><path d="M40 38V24h42v14M4 62h114"/><circle cx="61" cy="70" r="14"/><path d="M61 62v16M53 70h16"/><circle cx="112" cy="8" r="6"/><circle cx="10" cy="12" r="4"/>
    </svg>
    <div class="rule" style="left:83px;top:391px"></div>
    <h3 style="left:83px;top:408px">Medical-Grade<br>Protection</h3>
    <p style="left:86px;top:496px">Proven technology trusted by healthcare professionals to neutralize harmful pathogens.</p>
  </div>

  <div class="benefit">
    <svg class="abs" style="left:489px;top:233px" width="122" height="122" viewBox="0 0 122 122" fill="none" stroke="var(--icon-green)" stroke-width="2">
      <path d="M60 110C20 100 6 70 14 40c30 4 50 30 46 70z"/><path d="M60 110c30-10 46-40 40-70-30 6-44 34-40 70z"/><path d="M20 50l38 58M98 50L62 106"/><circle cx="50" cy="18" r="10"/><circle cx="72" cy="8" r="5"/>
    </svg>
    <div class="rule" style="left:497px;top:391px"></div>
    <h3 style="left:497px;top:408px">Comfortable<br>and Breathable</h3>
    <p style="left:501px;top:496px">Designed for all-day wear with comfort in mind, ensuring easy breathability without compromising protection.</p>
  </div>

  <div class="benefit">
    <svg class="abs" style="left:890px;top:233px" width="122" height="122" viewBox="0 0 122 122" fill="none" stroke="var(--icon-green)" stroke-width="2">
      <circle cx="61" cy="61" r="22"/><circle cx="61" cy="61" r="14"/><path d="M61 20v12M61 90v12M20 61h12M90 61h12M32 32l9 9M81 81l9 9M32 90l9-9M81 41l9-9"/><circle cx="110" cy="10" r="6"/>
    </svg>
    <div class="rule" style="left:897px;top:391px"></div>
    <h3 style="left:897px;top:408px">Sustainable<br>and Reusable</h3>
    <p style="left:900px;top:496px">Reusable design with eco-friendly materials, helping to reduce environmental impact.</p>
  </div>
</section>

<section class="healthcare">
  <h2 class="section-title" style="top:88px"><span class="accent">BrisaVeil</span> for Healthcare Providers</h2>
  <div class="art" role="img" aria-label="Photo of a doctor in a white coat with stethoscope and digital health interface" style="left:41px;top:126px;width:549px;height:448px;background:radial-gradient(ellipse at 45% 50%,#c9cbce 0%,#e3e4e6 50%,var(--paper) 78%)"></div>
  <div class="rule" style="left:617px;top:214px"></div>
  <p class="copy" style="left:617px;top:234px;width:490px">BrisaVeil offers healthcare providers an advanced option for protecting themselves and patients from airborne infections. Our Rose Bengal photosensitizer technology ensures a higher level of pathogen neutralization compared to traditional masks. Learn how BrisaVeil can help keep your practice safe.</p>
  <span class="btn btn-pink" style="left:613px;top:489px;width:168px;height:30px;line-height:30px">Request a Sample</span>
</section>

<section class="everyday">
  <div class="art" role="img" aria-label="Photo of a woman breathing fresh air outdoors" style="left:611px;top:163px;width:589px;height:448px;background:radial-gradient(ellipse at 55% 45%,#c6c9c7 0%,#dfe5e1 45%,var(--mint) 75%)"></div>
  <h2 class="section-title" style="top:124px;left:-5px"><span class="accent">BrisaVeil</span> for Everyday Protection</h2>
  <div class="rule" style="left:153px;top:264px"></div>
  <p class="copy" style="left:153px;top:284px;width:480px">BrisaVeil is designed for individuals who want added protection against airborne pathogens. With Rose Bengal technology, you can protect yourself and those around you while comfortably wearing a mask suitable for all-day use.</p>
  <span class="btn btn-pink" style="left:153px;top:494px;width:137px;height:30px;line-height:30px">Shop Now</span>
</section>

<section class="testimonials">
  <h2 class="section-title" style="top:90px">WHAT CUSTOMER ARE SAYING</h2>
  <div class="quote-mark" style="left:222px;top:210px">“</div>
  <div class="arrow" style="left:138px;top:316px;transform:rotate(135deg)"></div>
  <div class="arrow" style="left:1028px;top:316px;transform:rotate(-45deg)"></div>
  <div class="rule" style="left:301px;top:255px"></div>
  <p class="copy" style="left:301px;top:286px;width:610px;font-style:italic">Lorem ipsum dolor sit amet, consectetur adipisicing elit, sed do eiusmod tempor incididunt ut labore et dolore magna aliqua. Ut enim ad minim veniam, quis nostrud exercitation ullamco laboris nisi ut aliquip ex ea explicabo.</p>
  <div class="abs" style="left:301px;top:428px;font-size:16px;font-weight:700;color:var(--pink)">JONE DOE</div>
  <div class="abs" style="left:301px;top:460px;font-size:16px;font-weight:600;color:#777">Lorem ipsum dolor sit amet</div>
  <div class="quote-mark" style="left:904px;top:448px">”</div>
</section>

<section class="cta">
  <div class="cta-box">
    <p>Ready to experience the next level of protection with<br>BrisaVeil? Protect yourself, protect others.</p>
    <span class="btn" style="left:340px;top:154px;width:118px;height:26px;line-height:26px;background:#fff;color:var(--pink);font-size:10px">Shop Now</span>
  </div>
</section>

<footer class="site-footer">
  <span class="foot-link" style="left:151px;top:134px">Terms or Service</span>
  <span class="foot-link" style="left:151px;top:197px">Returns &amp; Refunds</span>
  <span class="foot-link" style="left:151px;top:260px">Privacy Policy</span>
  <span class="foot-link" style="left:151px;top:323px">About Us</span>
  <span class="foot-link" style="left:151px;top:384px">How It Works</span>
  <span class="foot-link" style="left:151px;top:447px">FAQs</span>

  <span class="foot-link" style="left:534px;top:134px">For Healthcare</span>
  <span class="foot-link" style="left:534px;top:197px">For Individuals</span>
  <span class="foot-link" style="left:534px;top:260px">Shop All</span>
  <span class="foot-link" style="left:534px;top:323px">Benefits</span>

  <span class="foot-link" style="left:866px;top:134px">Contact Information</span>
  <span class="foot-link" style="left:866px;top:197px">Follow us</span>
  <span class="social" style="left:866px;top:262px"></span>
  <span class="social" style="left:900px;top:262px"></span>
  <span class="social" style="left:934px;top:262px"></span>
  <span class="social" style="left:968px;top:262px"></span>

  <div class="abs foot-brand">BrisaVeil</div>
</footer>
<div class="abs foot-bar" style="left:0;width:1200px"><p>Copyright © 2024 BrisaVeil</p></div>

</body>
</html>
```